New Business Cards for NYC Salon

We are updating all of our cards. 7142-2869-4057 is my account number. We put names of our stylists on their cards. The back should include appointment space. Were looking for something more sleek and modern. Black/White Silver... or even touches of the orange color on our website which has been our thing for years. The design should communicate professional upscale boutique salon for men and women. Should be able to incorporate design into thank you cards, referral cards, brochure and postcards. The file is a zip file...we like the stacked ones black or white or the side versions.

Industry/Entity Type

Beauty Salon

Contact Information for Business Card

Marcus John's Salon313 W. 53rd Street, New York NY 10019 212-386-7714 info@marcusdellsalon.example www.marcusdellsalon.example

Font styles to use
Other font styles liked:
• trajan

Requirements
Must have
• we print a different card for every person in the salon. Begin by designing with the name Marcus. We will change it with every employee when printing. Must have a space for appointment date and time.
Nice to have
• Were looking to move towards the stacked or side placed logo but not opposed to utilizing the circular.
Should not have
• Photos

```html
<!DOCTYPE html>
<html lang="en">
<head>
<meta charset="utf-8">
<title>Marcus Dell's Salon – Business Cards</title>
<link rel="stylesheet" href="https://fonts.googleapis.com/css2?family=Cinzel:wght@400;600;700&display=swap">
<style>
  :root {
    --canvas: #e9e6e1;
    --card-white: #ffffff;
    --card-silver: #e4e4e4;
    --ink: #111111;
    --ink-soft: #3a3a3a;
    --black: #050505;
    --logo-silver: #b9b9b9;
    --shadow: rgba(0, 0, 0, 0.28);
  }
  * { box-sizing: border-box; margin: 0; padding: 0; }
  html, body {
    width: 1200px; height: 1023px; overflow: hidden;
    background: var(--canvas);
    font-family: "Cinzel", "Times New Roman", serif;
    color: var(--ink);
  }
  .canvas { position: relative; width: 1200px; height: 1023px; }

  .card {
    position: absolute;
    width: 700px; height: 400px;
    border-radius: 28px;
    overflow: hidden;
    box-shadow: 0 14px 34px var(--shadow);
  }

  /* Front */
  .card-front {
    left: 70px; top: 70px;
    background: linear-gradient(135deg, var(--card-white) 0%, var(--card-white) 55%, var(--card-silver) 100%);
  }
  .brand {
    position: absolute; left: 60px; top: 62px;
    display: flex; align-items: center; gap: 14px;
  }
  .brand-dot {
    width: 12px; height: 12px; border-radius: 50%;
    background: var(--ink);
  }
  .brand-name {
    font-size: 22px; font-weight: 400; letter-spacing: 5px;
    text-transform: uppercase; color: var(--ink);
  }
  .stylists {
    position: absolute; left: 60px; right: 50px; top: 172px;
    font-size: 21px; font-weight: 600; letter-spacing: 0;
    padding-bottom: 10px;
    border-bottom: 3px solid var(--ink);
    white-space: nowrap;
  }
  .contact {
    position: absolute; left: 60px; top: 228px;
    list-style: none;
    font-size: 17px; color: var(--ink-soft); line-height: 1.55;
  }
  .contact li { display: flex; align-items: center; gap: 10px; }
  .contact svg { width: 16px; height: 16px; flex: none; }
  .address {
    position: absolute; left: 60px; top: 318px;
    font-style: normal; font-size: 17px; color: var(--ink-soft); line-height: 1.4;
  }

  /* Back */
  .card-back {
    left: 440px; top: 560px;
    background: var(--card-white);
  }
  .back-band {
    position: absolute; left: 0; top: 0; width: 100%; height: 175px;
    background: var(--black);
    display: flex; align-items: center; justify-content: center; gap: 14px;
  }
  .back-band .brand-dot { background: var(--logo-silver); }
  .back-band .brand-name { color: var(--logo-silver); font-size: 20px; }
  .appointment {
    position: absolute; left: 40px; right: 40px; top: 205px;
  }
  .appointment-title {
    text-align: center; font-size: 26px; font-weight: 700; margin-bottom: 34px;
  }
  .fields { display: flex; gap: 22px; }
  .field {
    display: flex; align-items: flex-end; gap: 6px;
    font-size: 17px;
  }
  .field-name { flex: 1.25; }
  .field-date { flex: 1; }
  .field-time { flex: 1; }
  .field .dots {
    flex: 1; height: 1px;
    border-bottom: 2px dotted var(--ink);
    margin-bottom: 5px;
  }
</style>
</head>
<body>
<main class="canvas">

  <section class="card card-front" aria-label="Business card front">
    <div class="brand">
      <span class="brand-dot"></span>
      <span class="brand-name">Marcus Dell's Salon</span>
    </div>

    <h1 class="stylists">Marcus, Elena, June, Beatrice, Leandro, Nadia</h1>

    <ul class="contact">
      <li>
        <svg viewBox="0 0 16 16" aria-hidden="true"><path d="M2 5c0-2 1-3 6-3s6 1 6 3v1h-3V5H5v1H2z M4 7h8l1 6H3z" fill="#222"/><circle cx="8" cy="10" r="1.6" fill="#fff"/></svg>
        212-386-7714
      </li>
      <li>
        <svg viewBox="0 0 16 16" aria-hidden="true"><rect x="1" y="3" width="14" height="10" fill="#222"/><path d="M1 3l7 6 7-6M1 13l5-5M15 13l-5-5" stroke="#fff" stroke-width="1.2" fill="none"/></svg>
        info@marcusdellsalon.example
      </li>
      <li>
        <svg viewBox="0 0 16 16" aria-hidden="true"><circle cx="8" cy="8" r="7" fill="#222"/><path d="M1 8h14M8 1v14M3 4h10M3 12h10" stroke="#fff" stroke-width="0.9" fill="none"/><ellipse cx="8" cy="8" rx="3.2" ry="7" stroke="#fff" stroke-width="0.9" fill="none"/></svg>
        www.marcusdellsalon.example
      </li>
    </ul>

    <address class="address">
      748 E. 29th Street<br>
      New York NY 10016
    </address>
  </section>

  <section class="card card-back" aria-label="Business card back">
    <div class="back-band">
      <span class="brand-dot"></span>
      <span class="brand-name">Marcus Dell's Salon</span>
    </div>
    <div class="appointment">
      <h2 class="appointment-title">Next Appointment</h2>
      <div class="fields">
        <div class="field field-name">Name<span class="dots"></span></div>
        <div class="field field-date">Date<span class="dots"></span></div>
        <div class="field field-time">Time<span class="dots"></span></div>
      </div>
    </div>
  </section>

</main>
</body>
</html>
```